Electrical panel service sticker w Bucket truck & Logo

We have a rather plain sticker we put on lighting panels to remind customers who to call for service. We want to redesign them with brushed aluminum background. We want a remake of the sticker with the outline of a bucket truck. You'll need to find or draw the outling of a bucket truck maybe with the boom up slightly as we will get these stickers die cut.

We want LOGO with Ph.# and Email.
Electrical * Lighting * Sign Service

Target Market(s)

Commercial property managers

Industry/Entity Type

Property Management

Requirements
Must have
• Bucket Truck Outline

```html
<!DOCTYPE html>
<html lang="en">
<head>
<meta charset="utf-8">
<title>Brightline Service Co. – Panel Service Sticker</title>
<link href="https://fonts.googleapis.com/css2?family=Poppins:wght@500;700;800&display=swap" rel="stylesheet">
<style>
  :root {
    --brand-red: #a3000b;
    --brand-blue: #06298f;
    --ink: #111111;
    --white: #ffffff;
    --metal-light: #f4f5f6;
    --metal-mid: #d9dcdf;
    --metal-dark: #c4c8cc;
    --page: #ffffff;
  }
  * { margin: 0; padding: 0; box-sizing: border-box; }
  html, body {
    width: 1091px;
    height: 1200px;
    overflow: hidden;
    background: var(--page);
  }
  body {
    position: relative;
    font-family: "Poppins", sans-serif;
  }
  .sticker {
    position: absolute;
    left: 64px;
    top: 341px;
    width: 950px;
    height: 459px;
    overflow: hidden;
    background:
      linear-gradient(90deg,
        var(--metal-dark) 0%,
        var(--metal-light) 18%,
        var(--metal-mid) 35%,
        var(--metal-light) 55%,
        var(--metal-mid) 72%,
        var(--metal-light) 85%,
        var(--metal-dark) 100%);
  }
  .brand-name {
    position: absolute;
    left: 32px;
    top: 40px;
    width: 460px;
    text-align: center;
    color: var(--brand-red);
    font-weight: 800;
    font-size: 60px;
    line-height: 1.05;
    letter-spacing: 1px;
    text-transform: uppercase;
  }
  .service-list {
    position: absolute;
    left: 121px;
    top: 264px;
    list-style: none;
  }
  .service-list li {
    display: flex;
    align-items: center;
    height: 35px;
    font-weight: 800;
    font-size: 27px;
    letter-spacing: 2px;
    color: var(--ink);
  }
  .service-list .star {
    width: 26px;
    height: 26px;
    margin-right: 7px;
    fill: var(--brand-red);
  }
  .truck-art {
    position: absolute;
    left: 533px;
    top: 36px;
    width: 367px;
    height: 342px;
    border-radius: 10px;
    background: linear-gradient(160deg, #3b57b0 0%, var(--brand-blue) 100%);
    opacity: 0.85;
  }
  .contact-bar {
    position: absolute;
    left: 0;
    top: 0;
    width: 950px;
    height: 459px;
  }
  .email {
    position: absolute;
    left: 37px;
    top: 413px;
    font-weight: 500;
    font-size: 19px;
    color: var(--white);
    letter-spacing: 0.3px;
  }
  .phone {
    position: absolute;
    left: 501px;
    top: 387px;
    width: 418px;
    font-weight: 700;
    font-size: 54px;
    line-height: 1.2;
    letter-spacing: 4px;
    color: var(--white);
    white-space: nowrap;
  }
</style>
</head>
<body>
  <main class="sticker">
    <h1 class="brand-name">Brightline<br>Service Co.</h1>

    <ul class="service-list">
      <li><svg class="star" viewBox="0 0 24 24"><polygon points="12,1 15,9 23.5,9 16.7,14.2 19.2,22.5 12,17.5 4.8,22.5 7.3,14.2 0.5,9 9,9"/></svg>ELECTRICAL</li>
      <li><svg class="star" viewBox="0 0 24 24"><polygon points="12,1 15,9 23.5,9 16.7,14.2 19.2,22.5 12,17.5 4.8,22.5 7.3,14.2 0.5,9 9,9"/></svg>LIGHTING</li>
      <li><svg class="star" viewBox="0 0 24 24"><polygon points="12,1 15,9 23.5,9 16.7,14.2 19.2,22.5 12,17.5 4.8,22.5 7.3,14.2 0.5,9 9,9"/></svg>SIGN SERVICE</li>
    </ul>

    <div class="truck-art" role="img" aria-label="Blue outline of a bucket truck with its boom raised"></div>

    <svg class="contact-bar" viewBox="0 0 950 459" aria-hidden="true">
      <rect x="0" y="403" width="500" height="56" fill="var(--brand-red)"/>
      <polygon points="484,380 950,380 950,459 435,459" fill="var(--brand-blue)"/>
    </svg>

    <p class="email">Service@BrightlineService.com</p>
    <p class="phone">555.014.2290</p>
  </main>
</body>
</html>
```